Four in One (Flexible infographic for Content Management Industry)

See attachment.
A graphic depicting 4 products, where each can stand on its own and each can be combined with others, but where, if all are taken together, the best result is achieved (the "super product").
Intended use is web. See attached file as an example.
The most basic idea is as the attached diagram shows, where 4 rectangles are arranged in a quadrangle, with a middle rectangle in the center representing the combined 4 products. This concept is fine except it is a bit too obvious as it stands. We are looking for either a variation of this or another concept.
The audience is technical + professional + enterprise - NOT consumers. Hence the design should be conservative in nature.
We are aware of tools like as Canva or Pictogram where such graphics are available, but we are looking for something with a bit more imagination and flexibility.
This graphic should be targeted to web sites and be delivered with vector-based (SVG) graphics.

```html
<!DOCTYPE html>
<html lang="en">
<head>
<meta charset="utf-8">
<title>Four in One – Super Product</title>
<link href="https://fonts.googleapis.com/css2?family=Bebas+Neue&family=Poppins:wght@400&display=swap" rel="stylesheet">
<style>
  :root{
    --bg:#f7f7f7;
    --grid:#ebebeb;
    --ink:#2e2e2e;
    --body:#1f1f1f;
    --icon:#333333;
    --muted:#9a9a9a;
    --green:#86f03f;
    --teal:#dcf6f1;
    --mint:#e6f9d9;
    --card:#ffffff;
    --tile-top:#ffffff;
    --tile-bottom:#e9e9e9;
  }
  *{box-sizing:border-box;margin:0;padding:0}
  html,body{width:1200px;height:675px;overflow:hidden}
  body{
    position:relative;
    background-color:var(--bg);
    background-image:
      linear-gradient(var(--grid) 1px, transparent 1px),
      linear-gradient(90deg, var(--grid) 1px, transparent 1px);
    background-size:67.5px 67.5px;
    background-position:4px 0;
    font-family:"Poppins",sans-serif;
    color:var(--body);
  }
  .abs{position:absolute}
  .decor{position:absolute;left:0;top:0}

  .hub-frame{
    left:372px;top:150px;width:462px;height:359px;
    border:6px solid #ededed;border-radius:4px;
    box-shadow:0 0 0 1px #fafafa inset;
  }
  .hub{
    left:387px;top:159px;width:435px;height:338px;
    background:linear-gradient(150deg,#fdfdfd 0%,#ececec 100%);
    box-shadow:0 6px 18px rgba(0,0,0,.10);
  }
  .hub-title{
    position:absolute;left:0;width:435px;top:106px;
    font-family:"Bebas Neue",sans-serif;font-weight:400;color:var(--ink);
    font-size:78px;line-height:72px;text-align:center;
    padding-right:40px;
  }

  .info-card{
    background:var(--card);border-radius:16px;
    box-shadow:0 10px 28px rgba(0,0,0,.06);
  }
  .info-text{position:absolute;font-size:8.6px;line-height:11.8px;white-space:nowrap}
  .info-text p{margin-bottom:9px}
  .checks{list-style:none}
  .checks li{display:flex;align-items:center;gap:5px;height:12.2px}
  .checks svg{flex:none}

  .tile{
    background:linear-gradient(160deg,var(--tile-top) 0%,var(--tile-bottom) 100%);
    border-radius:14px;
    box-shadow:0 8px 22px rgba(0,0,0,.14);
  }
  .tile-title{
    position:absolute;font-family:"Bebas Neue",sans-serif;font-weight:400;color:var(--ink);
    font-size:31px;line-height:27.5px;white-space:nowrap;
  }
  .center{text-align:center}

  .soft-square{background:linear-gradient(160deg,#f1f1f1,#e4e4e4);border-radius:8px}
</style>
</head>
<body>
  <svg class="decor" width="1200" height="675" aria-hidden="true">
    <circle cx="834" cy="106" r="53" fill="none" stroke="var(--teal)" stroke-width="18"/>
    <circle cx="222" cy="478" r="53" fill="none" stroke="var(--mint)" stroke-width="18"/>
    <circle cx="347" cy="562" r="48" fill="none" stroke="#ececec" stroke-width="16"/>
    <symbol id="tick" viewBox="0 0 10 10"><circle cx="5" cy="5" r="4.2" fill="none" stroke="#333" stroke-width="1"/><path d="M3 5.2l1.4 1.4L7 3.8" fill="none" stroke="#333" stroke-width="1"/></symbol>
  </svg>

  <div class="abs soft-square" style="left:242px;top:216px;width:70px;height:71px"></div>
  <div class="abs soft-square" style="left:869px;top:224px;width:53px;height:42px;opacity:.6"></div>

  <div class="abs hub-frame"></div>
  <div class="abs hub"><h1 class="hub-title">Super<br>Product</h1></div>

  <!-- Document management -->
  <section class="abs info-card" style="left:131px;top:73px;width:208px;height:130px">
    <div class="info-text" style="left:13px;top:14px">
      <p>Streamline document organization,<br>acces, and collaboration with easier<br>file storage and&nbsp; sharing, leading to<br>more effiecient workflows.</p>
      <ul class="checks">
        <li><svg width="8" height="8"><use href="#tick"/></svg>Centralized Document control</li>
        <li><svg width="8" height="8"><use href="#tick"/></svg>Collaborative Workspace Integration</li>
        <li><svg width="8" height="8"><use href="#tick"/></svg>Automated Compliance Tracking</li>
        <li><svg width="8" height="8"><use href="#tick"/></svg>Check 4</li>
      </ul>
    </div>
  </section>
  <section class="abs tile" style="left:321px;top:131px;width:209px;height:90px">
    <svg class="abs" style="left:20px;top:25px" width="34" height="46" viewBox="0 0 34 46" aria-hidden="true">
      <path d="M1.5 1.5h22l9 9v34h-31z" fill="none" stroke="#9a9a9a" stroke-width="2"/>
      <path d="M23.5 1.5v9h9" fill="none" stroke="#9a9a9a" stroke-width="2"/>
      <path d="M7 11h6" stroke="#9a9a9a" stroke-width="2"/>
      <path d="M7 24h20M7 30h20M7 36h20" stroke="var(--green)" stroke-width="2.4"/>
    </svg>
    <h2 class="tile-title" style="left:71px;top:22px">Document<br>Management</h2>
  </section>

  <!-- Security & compliance -->
  <section class="abs info-card" style="left:819px;top:76px;width:247px;height:135px">
    <div class="info-text" style="left:63px;top:15px">
      <p>Benefit from tailored cloud solutions,<br>secure data storage, and expert disas-<br>ter recovery planning for reliable and<br>scalable IT operations.</p>
      <ul class="checks">
        <li><svg width="8" height="8"><use href="#tick"/></svg>Custom cloud solutions</li>
        <li><svg width="8" height="8"><use href="#tick"/></svg>Secure Data Storage</li>
        <li><svg width="8" height="8"><use href="#tick"/></svg>Expert Disaster Recovery</li>
        <li><svg width="8" height="8"><use href="#tick"/></svg>Check 4</li>
      </ul>
    </div>
  </section>
  <section class="abs tile" style="left:736px;top:124px;width:133px;height:137px">
    <svg class="abs" style="left:48px;top:15px" width="44" height="44" viewBox="0 0 44 44" aria-hidden="true">
      <path d="M9 16V9a8 8 0 0 1 16 0v5" fill="none" stroke="#9a9a9a" stroke-width="2.4"/>
      <path d="M3 16h26M3 16v24h12" fill="none" stroke="#9a9a9a" stroke-width="2.4"/>
      <path d="M19 40h19a5 5 0 0 0 0-10 7 7 0 0 0-13-3 6 6 0 0 0-6 13z" fill="none" stroke="var(--green)" stroke-width="2.4" stroke-linejoin="round"/>
    </svg>
    <h2 class="tile-title center" style="left:0;width:133px;top:72px">Security &amp;<br>Compliance</h2>
  </section>

  <!-- Enterprise resource planning -->
  <section class="abs info-card" style="left:104px;top:460px;width:244px;height:129px">
    <div class="info-text" style="left:18px;top:15px">
      <p>Simply management across finance, sales<br>and operations, enabling better decision<br>making and improved productivity.</p>
      <ul class="checks">
        <li><svg width="8" height="8"><use href="#tick"/></svg>Integrated Business Processes</li>
        <li><svg width="8" height="8"><use href="#tick"/></svg>Enhanced Decision-Making</li>
        <li><svg width="8" height="8"><use href="#tick"/></svg>Productivity Improvement</li>
        <li><svg width="8" height="8"><use href="#tick"/></svg>Check 4</li>
      </ul>
    </div>
  </section>
  <section class="abs tile" style="left:317px;top:376px;width:155px;height:185px">
    <svg class="abs" style="left:54px;top:24px" width="46" height="44" viewBox="0 0 46 44" aria-hidden="true">
      <rect x="1" y="2" width="19" height="18" fill="#9e9e9e"/>
      <rect x="1" y="25" width="19" height="18" fill="#9e9e9e"/>
      <rect x="24" y="25" width="19" height="18" fill="#9e9e9e"/>
      <path d="M33.5 0L45 11.5 33.5 23 22 11.5z" fill="var(--green)"/>
    </svg>
    <h2 class="tile-title center" style="left:0;width:155px;top:87px">Enterprise<br>Resource<br>Planning</h2>
  </section>

  <!-- Digital transformation -->
  <section class="abs info-card" style="left:842px;top:446px;width:241px;height:135px">
    <div class="info-text" style="left:47px;top:21px">
      <p style="margin-bottom:0">Turn scanned documents into easily<br>searchable digital archives, boost-<br>ing<br>efficiency and accessibility.</p>
      <ul class="checks">
        <li><svg width="8" height="8"><use href="#tick"/></svg>Instand searchable Archieves with OCR</li>
        <li><svg width="8" height="8"><use href="#tick"/></svg>Automated Docu ment Classification</li>
        <li><svg width="8" height="8"><use href="#tick"/></svg>Kelbrin Share and Cloud Blob Ready</li>
        <li><svg width="8" height="8"><use href="#tick"/></svg>Check 4</li>
      </ul>
    </div>
  </section>
  <section class="abs tile" style="left:609px;top:455px;width:261px;height:89px">
    <svg class="abs" style="left:12px;top:14px" width="62" height="62" viewBox="0 0 62 62" aria-hidden="true">
      <g stroke="#9a9a9a" stroke-width="2">
        <path d="M31 3v12M31 47v12M3 31h12M47 31h12M11 11l9 9M42 42l9 9M51 11l-9 9M20 42l-9 9"/>
      </g>
      <g fill="var(--green)">
        <circle cx="31" cy="3" r="2.4"/><circle cx="31" cy="59" r="2.4"/>
        <circle cx="3" cy="31" r="2.4"/><circle cx="59" cy="31" r="2.4"/>
        <circle cx="11" cy="11" r="2.4"/><circle cx="51" cy="51" r="2.4"/>
        <circle cx="51" cy="11" r="2.4"/><circle cx="11" cy="51" r="2.4"/>
      </g>
      <g fill="none" stroke="var(--green)" stroke-width="2.4">
        <circle cx="31" cy="31" r="15"/>
        <ellipse cx="31" cy="31" rx="6.5" ry="15"/>
        <path d="M16 31h30M18 24h26M18 38h26"/>
      </g>
    </svg>
    <h2 class="tile-title" style="left:86px;top:17px">Digital<br>Transformation</h2>
  </section>
</body>
</html>
```